BrovaLT BIZ Card, email signature & Stationary

Professional business cards, email signatures and ms word letterhead

Target Market(s)

business owners

Industry/Entity Type

cloud hosting

Contact Information for Business Card

name title office phone number , direct line, fax email address web site

Font styles to use
Other font styles liked:
• something that compliments font in logo

```html
<!DOCTYPE html>
<html lang="en">
<head>
<meta charset="utf-8">
<title>BrovaLT Business Card</title>
<link rel="stylesheet" href="https://fonts.googleapis.com/css2?family=Poppins:wght@400;600&display=swap">
<style>
  :root {
    --page-bg: #e8e3dc;
    --brand-red: #c8141c;
    --brand-red-dark: #a00a10;
    --ink: #161616;
    --card-silver-light: #f7f8f9;
    --card-silver-mid: #dcdfe2;
    --name-tint: #f3dccd;
    --text-dark: #2a2a2a;
  }
  html, body {
    margin: 0;
    width: 1200px;
    height: 970px;
    overflow: hidden;
    background: var(--page-bg);
    font-family: "Poppins", sans-serif;
  }
  .stage {
    width: 1200px;
    height: 970px;
    display: flex;
    align-items: center;
    justify-content: center;
  }
  .business-card {
    width: 1000px;
    height: 569px;
    border-radius: 34px;
    overflow: hidden;
    box-shadow: 0 14px 40px rgba(0,0,0,0.18);
  }
  .business-card svg { display: block; width: 100%; height: 100%; }
  .card-name { font-family: "Poppins", sans-serif; font-weight: 600; font-size: 38px; fill: var(--name-tint); letter-spacing: 0.5px; }
  .card-title { font-family: "Poppins", sans-serif; font-weight: 400; font-size: 23px; fill: #ffffff; }
  .brand-name { font-family: "Poppins", sans-serif; font-weight: 400; font-size: 148px; fill: var(--brand-red); }
  .contact-line { font-family: "Poppins", sans-serif; font-weight: 400; font-size: 29px; fill: var(--text-dark); }
  .contact-icon { fill: var(--brand-red); }
  .icon-glyph { fill: none; stroke: #ffffff; stroke-width: 2.2; stroke-linecap: round; stroke-linejoin: round; }
</style>
</head>
<body>
<main class="stage">
  <article class="business-card">
    <svg viewBox="0 0 1178 670" preserveAspectRatio="none" xmlns="http://www.w3.org/2000/svg">
      <defs>
        <linearGradient id="card-face" x1="0" y1="0" x2="1" y2="1">
          <stop offset="0" stop-color="var(--card-silver-light)"/>
          <stop offset="0.5" stop-color="#eceef0"/>
          <stop offset="1" stop-color="var(--card-silver-mid)"/>
        </linearGradient>
        <linearGradient id="red-band" x1="0" y1="0" x2="1" y2="0">
          <stop offset="0" stop-color="var(--brand-red)"/>
          <stop offset="0.6" stop-color="var(--brand-red-dark)"/>
          <stop offset="1" stop-color="var(--brand-red)"/>
        </linearGradient>
      </defs>

      <rect class="card-face" width="1178" height="670" fill="url(#card-face)"/>

      <rect class="header-band" x="0" y="0" width="1178" height="165" fill="url(#red-band)"/>
      <rect class="header-rule" x="0" y="165" width="1178" height="8" fill="var(--ink)"/>

      <text class="card-name" x="1110" y="90" text-anchor="end">DANIEL R HALE</text>
      <text class="card-title" x="1110" y="127" text-anchor="end">CEO</text>

      <text class="brand-name" x="62" y="405">BrovaLT</text>

      <line class="contact-rule" x1="66" y1="485" x2="1110" y2="485" stroke="var(--ink)" stroke-width="2"/>
      <line class="contact-divider" x1="508" y1="522" x2="508" y2="632" stroke="var(--ink)" stroke-width="2"/>

      <g class="contact-phones">
        <circle class="contact-icon" cx="84" cy="535" r="16"/>
        <path class="icon-glyph" d="M78,527 l4,-2 3,6 -2,2 c1,3 3,5 6,6 l2,-2 6,3 -2,4 c-9,0 -17,-8 -17,-17z"/>
        <text class="contact-line" x="114" y="545">(555) 214-3086</text>

        <circle class="contact-icon" cx="84" cy="575" r="16"/>
        <rect class="icon-glyph" x="79" y="566" width="10" height="18" rx="2"/>
        <text class="contact-line" x="114" y="585">(555) 214-3087</text>

        <circle class="contact-icon" cx="84" cy="615" r="16"/>
        <rect class="icon-glyph" x="76" y="611" width="16" height="9" rx="1"/>
        <rect class="icon-glyph" x="79" y="605" width="10" height="6"/>
        <text class="contact-line" x="114" y="625">(555) 214-3088</text>
      </g>

      <g class="contact-online">
        <circle class="contact-icon" cx="686" cy="575" r="16"/>
        <rect class="icon-glyph" x="677" y="568" width="18" height="13" rx="1"/>
        <path class="icon-glyph" d="M677,569 l9,7 9,-7"/>
        <text class="contact-line" x="718" y="585">info@brovaltmail.com</text>

        <circle class="contact-icon" cx="686" cy="615" r="16"/>
        <circle class="icon-glyph" cx="686" cy="615" r="9"/>
        <path class="icon-glyph" d="M677,615 h18 M686,606 c-5,5 -5,13 0,18 c5,-5 5,-13 0,-18"/>
        <text class="contact-line" x="718" y="625">www.brovaltweb.com</text>
      </g>
    </svg>
  </article>
</main>
</body>
</html>
```